Business Card Design needed for logo design project

This project is linked to Consulting Firm + Meeting Space needs logo and bus card..
Our company needs a Business Card Design. Please refer to our original project in the link above.
Industry/Entity Type
Business

```html
<!DOCTYPE html>
<html lang="en">
<head>
<meta charset="utf-8">
<title>Tidewell Business Card</title>
<link rel="stylesheet" href="https://fonts.googleapis.com/css2?family=Open+Sans:wght@300;400;700&display=swap">
<style>
  :root {
    --page-bg: #e9ebee;
    --card-white: #f4f6f8;
    --ink-blue: #2a5d9c;
    --ink-soft: #4d76aa;
    --brand-blue: #2b86c8;
    --tone-light: #dbe4f4;
    --tone-mid: #a9bde6;
    --tone-deep: #6f8fcf;
  }
  * { margin: 0; padding: 0; box-sizing: border-box; }
  html, body {
    width: 1200px;
    height: 873px;
    overflow: hidden;
    background: var(--page-bg);
    font-family: "Open Sans", sans-serif;
  }
  .sheet {
    width: 1200px;
    height: 873px;
    display: flex;
    align-items: center;
    justify-content: center;
    gap: 60px;
  }
  .card {
    width: 520px;
    height: 297px;
    border-radius: 3px;
    box-shadow: 0 6px 18px rgba(40, 60, 90, 0.18);
    overflow: hidden;
    position: relative;
  }
  .card-front {
    background: var(--card-white);
    color: var(--ink-blue);
    padding: 34px 40px;
  }
  .person-name {
    font-weight: 700;
    font-size: 19px;
    letter-spacing: 0.2px;
  }
  .person-role {
    font-size: 12px;
    color: var(--ink-soft);
    margin-top: 4px;
  }
  .contact-list {
    list-style: none;
    margin-top: 16px;
    font-size: 12px;
    line-height: 1.6;
    color: var(--ink-soft);
  }
  .brand-name {
    position: absolute;
    right: 40px;
    bottom: 32px;
    font-weight: 300;
    font-size: 58px;
    line-height: 1.2;
    letter-spacing: -0.5px;
    color: var(--ink-blue);
  }
  .card-back-art {
    width: 100%;
    height: 100%;
    background: linear-gradient(30deg, var(--tone-deep) 0%, var(--tone-mid) 35%, var(--tone-light) 62%, var(--brand-blue) 88%);
  }
</style>
</head>
<body>
<main class="sheet">
  <section class="card card-front">
    <h1 class="person-name">Evan Marsh</h1>
    <p class="person-role">Founder &amp; CEO</p>
    <ul class="contact-list">
      <li>T: (555) 014 229</li>
      <li>M: hello@tidewell.com</li>
      <li>W: tidewell.com</li>
    </ul>
    <p class="brand-name">Tidewell</p>
  </section>

  <section class="card card-back">
    <div class="card-back-art" role="img" aria-label="Blue layered wave illustration filling the card back"></div>
  </section>
</main>
</body>
</html>
```